Affiliate marketing network landing page

We need a landing page for an affiliate marketing company called Brindle Harbor.

Our primary offering will be a CPA (cost per action) affiliate network with emphasis on treating our affiliates EPC's "royally".

We would like the final design to be clean and minimal similar to the aesthetic of velmora.com or quorvanexis.com.

Some of our competitors/other companies in the industry for inspiration would be tandurifo.com, meadowlinkers.com, brovintel.com, dornvault.com, haltorigrid.com, punwickery.com, ozmelquin.com to name a few in no particular order.

Should you propose the winning design, we would like you to build it just in HTML/CSS (not to be integrated into a CMS) - but we can discuss the specifics of that when the time comes.

Attached is the logo that should be used both on the site and as inspiration for the design (colors, aesthetic, etc).

```html
<!DOCTYPE html>
<html lang="en">
<head>
<meta charset="utf-8">
<title>Brindle Harbor — Affiliate Marketing Company</title>
<link rel="stylesheet" href="https://fonts.googleapis.com/css2?family=Roboto:ital,wght@0,400;0,500;0,700;0,900;1,400&display=swap">
<style>
:root{
  --ink:#000;
  --night:#08090c;
  --navy:#0d1120;
  --accent:#1c2150;
  --grey-btn:#8a8b8e;
  --text:#1b1b1b;
  --muted:#777a80;
  --line:#d8d9dc;
  --band:#e4e5e7;
  --footer:#1d1e20;
  --star:#f2b705;
}
*{box-sizing:border-box;margin:0;padding:0}
html,body{width:1200px;height:4815px;overflow:hidden}
body{position:relative;font-family:'Roboto',sans-serif;color:var(--text);background:#fff}
.abs{position:absolute}
.center{text-align:center}

/* hero */
.hero{position:absolute;left:0;top:0;width:1200px;height:686px;background:radial-gradient(ellipse at 50% 100%,#2a2c33 0%,#0c0d10 45%,#000 75%);color:#fff;overflow:hidden}
.hero-wave{position:absolute;left:0;bottom:0;width:1200px;height:230px;background:linear-gradient(180deg,rgba(0,0,0,0) 0%,rgba(90,92,100,.35) 70%,rgba(40,41,46,.6) 100%)}
.brand{position:absolute;font-weight:900;color:#fff;letter-spacing:.5px}
.nav{position:absolute;left:380px;top:38px;display:flex;gap:31px;font-size:13px;font-weight:700}
.nav span{color:#fff}
.btn-grey{position:absolute;background:var(--grey-btn);color:#fff;font-size:12px;font-weight:700;display:flex;align-items:center;justify-content:center;gap:8px;border-radius:3px}
.arrow-dot{width:12px;height:12px;border-radius:50%;background:#fff;display:inline-flex;align-items:center;justify-content:center}
.arrow-dot svg{width:7px;height:7px}
.hero h1{position:absolute;left:0;width:1200px;top:160px;text-align:center;font-size:40px;font-weight:700;letter-spacing:1px}
.hero .lead{position:absolute;left:0;width:1200px;top:226px;text-align:center;font-size:16px}
.net-title{position:absolute;top:328px;width:400px;text-align:center;font-size:44px;font-weight:500;letter-spacing:.5px}
.vline{position:absolute;top:389px;width:2px;height:22px;background:#888}
.net-card{position:absolute;top:440px;width:150px;height:171px;background:#050506;text-align:center;padding-top:16px}
.net-card h4{font-size:13px;font-weight:700}
.net-card p{font-size:11px;line-height:18px;margin-top:12px;padding:0 12px}
.net-card .join{display:inline-block;margin-top:14px;width:68px;height:22px;line-height:22px;background:var(--grey-btn);font-size:9px;font-weight:700;border-radius:2px}
.hub{position:absolute;left:574px;top:346px;width:52px;height:52px;border-radius:50%;border:2px solid #555;background:#111;display:flex;align-items:center;justify-content:center}

/* path */
.section-title{position:absolute;left:0;width:1200px;text-align:center;font-size:34px;font-weight:700;color:var(--ink)}
.path-intro{position:absolute;left:100px;width:1000px;top:876px;text-align:center;font-size:15px;line-height:26px;color:var(--muted)}
.illus{position:absolute;border-radius:14px}
.path-col{position:absolute;top:1178px;width:440px;text-align:center}
.path-col h3{font-size:20px;font-weight:500}
.path-col .rule{width:34px;height:3px;background:var(--accent);margin:14px auto 0}
.path-col p{margin-top:26px;font-size:13px;line-height:25px;color:var(--muted);text-align:justify;text-align-last:center}
.btn-black{position:absolute;background:#000;color:#fff;font-size:12px;font-weight:700;display:flex;align-items:center;justify-content:center;gap:10px;border-radius:2px}

/* about */
.about-bg{position:absolute;left:0;top:1467px;width:1200px;height:669px}
.about h2{position:absolute;left:114px;top:1636px;font-size:34px;font-weight:700;color:#fff}
.about p{position:absolute;left:114px;top:1698px;width:490px;font-size:13px;line-height:25.6px;color:#fff;text-align:justify}

/* focus */
.focus-card{position:absolute;width:307px;height:190px;border:1px solid var(--line);background:#fff}
.focus-card h4{position:absolute;left:24px;top:60px;font-size:15px;font-weight:700}
.focus-card p{position:absolute;left:24px;top:92px;width:270px;font-size:12.5px;line-height:24px;color:var(--muted)}
.focus-icon{position:absolute;width:76px;height:76px;background:#000;display:flex;align-items:center;justify-content:center}

/* stats */
.stats{position:absolute;left:0;top:2931px;width:1200px;height:456px;background:var(--band)}
.stat{position:absolute;top:3088px;width:238px;height:213px;background:#fff;padding:10px;box-shadow:0 2px 6px rgba(0,0,0,.08)}
.stat .inner{width:100%;height:100%;border:2px solid var(--navy);text-align:center;position:relative}
.stat h5{margin-top:18px;font-size:16px;font-weight:500}
.stat .num{position:absolute;left:0;right:0;bottom:16px;font-size:30px;font-weight:700}
.stat svg{margin-top:14px}

/* testimonials */
.skyline{position:absolute;left:40px;top:3813px;width:1120px;height:149px;background:linear-gradient(180deg,#eeeff1,#dcdde0)}
.quote{position:absolute;top:3570px;width:320px;height:252px;background:#fff;border:1px solid #e3e4e7}
.avatar{position:absolute;left:30px;top:28px;width:64px;height:64px;border-radius:50%;background:linear-gradient(135deg,#d9c3b0,#8f6f5a)}
.quote h6{position:absolute;left:122px;top:50px;font-size:15px;font-weight:700}
.quote .role{position:absolute;left:122px;top:70px;font-size:13px;color:var(--muted)}
.quote p{position:absolute;left:24px;top:120px;width:280px;font-size:13px;line-height:23px;font-style:italic;color:var(--muted)}
.stars{position:absolute;left:24px;top:208px;color:var(--star);font-size:14px;letter-spacing:2px}
.qmark{position:absolute;right:22px;top:196px;font-size:46px;font-weight:900;line-height:1}
.dots{position:absolute;left:570px;top:3869px;display:flex;gap:3px}
.dots i{width:8px;height:8px;border-radius:50%;background:#111;display:block}

/* contact */
.contact{position:absolute;left:0;top:3962px;width:1200px;height:556px;background:radial-gradient(ellipse at 50% 40%,#1a1b1f 0%,#050506 70%)}
.frame{position:absolute;left:254px;top:4060px;width:692px;height:375px;border:2px solid #8a8b8e;border-radius:6px}
.contact h2{position:absolute;left:452px;top:4036px;width:296px;background:#0c0d0f;text-align:center;font-size:38px;font-weight:700;color:#fff}
.field{position:absolute;background:#8a8b8e;color:#cfd0d2;font-size:13px;padding:14px 16px;border-radius:2px}

/* footer */
.footer{position:absolute;left:0;top:4518px;width:1200px;height:297px;background:var(--footer);color:#fff}
.footer h6{position:absolute;font-size:13px;font-weight:700}
.footer .item{position:absolute;font-size:13px;display:flex;align-items:center;gap:14px}
.social{position:absolute;top:4663px;width:34px;height:34px}
</style>
</head>
<body>

<!-- HERO -->
<section class="hero">
  <div class="hero-wave" role="img" aria-label="Abstract glowing particle wave"></div>
  <div class="brand" style="left:112px;top:28px;font-size:26px;line-height:30px">Brindle<br><span style="font-size:13px;letter-spacing:5px;font-weight:700">HARBOR</span></div>
  <nav class="nav"><span>HOME</span><span>ABOUT</span><span>PUBLISHERS</span><span>ADVERTISERS</span><span>CONTACT</span></nav>
  <div class="btn-grey" style="left:862px;top:28px;width:101px;height:39px">LOG IN <span class="arrow-dot"><svg viewBox="0 0 8 8"><path d="M3 1l3 3-3 3" stroke="#8a8b8e" stroke-width="1.6" fill="none"/></svg></span></div>
  <div class="btn-grey" style="left:981px;top:28px;width:103px;height:39px">SIGN UP <span class="arrow-dot"><svg viewBox="0 0 8 8"><path d="M3 1l3 3-3 3" stroke="#8a8b8e" stroke-width="1.6" fill="none"/></svg></span></div>

  <h1>Affiliate Marketing Company</h1>
  <p class="lead">Lorem ipsum dolor sit amet, consectetur adipiscing elit, sed do eiusmod tempor incididunt ut labore</p>

  <div class="net-title" style="left:105px">CPA NETWORK</div>
  <div class="net-title" style="left:696px">SMART LINK</div>
  <div class="hub"><svg width="14" height="20" viewBox="0 0 14 20"><path d="M7 2v14M2 11l5 6 5-6" stroke="#fff" stroke-width="2" fill="none"/></svg></div>

  <div class="vline" style="left:201px"></div><div class="vline" style="left:392px"></div>
  <div class="vline" style="left:793px"></div><div class="vline" style="left:983px"></div>

  <div class="net-card" style="left:127px"><h4>PUBLISHERS</h4><p>Sed ut perspiciatis unde omnis iste natus error sit voluptat</p><span class="join">JOIN NOW</span></div>
  <div class="net-card" style="left:318px"><h4>ADVERTISERS</h4><p>Sed ut perspiciatis unde omnis iste natus error sit volupta</p><span class="join">JOIN NOW</span></div>
  <div class="net-card" style="left:718px"><h4>PUBLISHERS</h4><p>Sed ut perspiciatis unde omnis iste natus error sit voluptat</p><span class="join">JOIN NOW</span></div>
  <div class="net-card" style="left:908px"><h4>ADVERTISERS</h4><p>Sed ut perspiciatis unde omnis iste natus error sit volupta</p><span class="join">JOIN NOW</span></div>
</section>

<!-- PATH -->
<h2 class="section-title" style="top:770px;line-height:44px">Your Path to Success Online<br>Starts Here.</h2>
<p class="path-intro">Lorem ipsum dolor sit amet, consectetur adipiscing elit, sed do eiusmod tempor incididunt ut labore et dolore magna aliqua.<br>Ut enim ad minim veniam, quis nostrud exercitation ullamco</p>

<div class="illus" style="left:243px;top:985px;width:237px;height:159px;background:linear-gradient(135deg,#3c5bd6,#e9eefc)" role="img" aria-label="Illustration of partners shaking hands in front of a monitor"></div>
<svg class="abs" style="left:552px;top:1005px" width="96" height="130" viewBox="0 0 96 130"><polygon points="36,0 96,0 60,130 0,130" fill="#000"/><polygon points="30,10 36,0 2,122 0,130" fill="#bbb"/></svg>
<div class="illus" style="left:760px;top:985px;width:162px;height:159px;background:linear-gradient(135deg,#e9eefc,#3c5bd6 70%,#f2a54a)" role="img" aria-label="Illustration of a shopper with a phone storefront and parcels"></div>

<div class="path-col" style="left:137px"><h3>Become An Affiliate</h3><div class="rule"></div>
<p>Sed ut perspiciatis unde omnis iste natus error sit voluptatem accusantium doloremque laudantium, totam rem aperiam, eaque ipsa quae ab illo inventore veritatis et quasi architecto beatae vitae dicta sunt explicabo. Nemo enim ipsam voluptatem</p></div>
<div class="path-col" style="left:623px"><h3>Sell Your Product</h3><div class="rule"></div>
<p>Sed ut perspiciatis unde omnis iste natus error sit voluptatem accusantium doloremque laudantium, totam rem aperiam, eaque ipsa quae ab illo inventore veritatis et quasi architecto beatae vitae dicta sunt explicabo. Nemo enim ipsam voluptatem</p></div>

<div class="btn-black" style="left:240px;top:1364px;width:234px;height:46px">BECOME AN AFFILIATE <span class="arrow-dot"><svg viewBox="0 0 8 8"><path d="M3 1l3 3-3 3" stroke="#000" stroke-width="1.6" fill="none"/></svg></span></div>
<div class="btn-black" style="left:726px;top:1364px;width:234px;height:46px">SELL YOUR PRODUCT <span class="arrow-dot"><svg viewBox="0 0 8 8"><path d="M3 1l3 3-3 3" stroke="#000" stroke-width="1.6" fill="none"/></svg></span></div>

<!-- ABOUT -->
<section class="about">
  <svg class="about-bg" viewBox="0 0 1200 669" preserveAspectRatio="none">
    <defs><linearGradient id="aboutGrad" x1="0" y1="0" x2="1" y2="1"><stop offset="0" stop-color="#0a0c14"/><stop offset="1" stop-color="#121a2e"/></linearGradient></defs>
    <polygon points="0,113 1200,0 1200,523 0,669" fill="url(#aboutGrad)"/>
  </svg>
  <h2>About Us</h2>
  <p>At vero eos et accusamus et iusto odio dignissimos ducimus qui blanditiis praesentium voluptatum deleniti atque corrupti quos dolores et quas molestias excepturi sint occaecati cupiditate non provident, similique sunt in culpa qui officia deserunt mollitia animi, id est laborum et dolorum fuga. Et harum quidem rerum facilis est et expedita distinctio. Nam libero tempore, cum soluta nobis est eligendi optio cumque nihil impedit quo minus id quod maxime placeat facere possimus, omnis voluptas assumenda est, omnis dolor repellendus. Temporibus autem quibusdam et aut officiis debitis aut rerum necessitatibus saepe eveniet ut et voluptates</p>
  <div class="btn-grey" style="left:114px;top:1957px;width:234px;height:45px;border-radius:2px">PUBLISHERS APPLY NOW <span class="arrow-dot"><svg viewBox="0 0 8 8"><path d="M3 1l3 3-3 3" stroke="#8a8b8e" stroke-width="1.6" fill="none"/></svg></span></div>
  <div class="btn-grey" style="left:363px;top:1957px;width:234px;height:45px;border-radius:2px">ADVISERS APPLY NOW <span class="arrow-dot"><svg viewBox="0 0 8 8"><path d="M3 1l3 3-3 3" stroke="#8a8b8e" stroke-width="1.6" fill="none"/></svg></span></div>
  <div class="illus" style="left:636px;top:1663px;width:499px;height:281px;background:radial-gradient(ellipse at 50% 55%,#7a6ee0 0%,#3d3b8f 45%,rgba(18,26,46,0) 75%)" role="img" aria-label="Isometric illustration of an online marketplace with shoppers, coins and a storefront"></div>
</section>

<!-- FOCUS -->
<h2 class="section-title" style="top:2220px">Our Focus Area</h2>

<div class="focus-card" style="left:112px;top:2370px"><h4>Pay Per Lead</h4><p>At vero eos et accusamus et iudignissimos ducimus qui blanditiis praesentiuoluptatum deleniti atque corruptidolores</p></div>
<div class="focus-card" style="left:456px;top:2370px"><h4>Pay Per Sale</h4><p>At vero eos et accusamus et iudignissimos ducimus qui blanditiis praesentiuoluptatum deleniti atque corruptidolores</p></div>
<div class="focus-card" style="left:798px;top:2370px"><h4>Pay Per Click</h4><p>At vero eos et accusamus et iudignissimos ducimus qui blanditiis praesentiuoluptatum deleniti atque corruptidolores</p></div>
<div class="focus-card" style="left:112px;top:2636px"><h4>Traffic Management</h4><p>At vero eos et accusamus et iudignissimos ducimus qui blanditiis praesentiuoluptatum deleniti atque corruptidolores</p></div>
<div class="focus-card" style="left:456px;top:2636px"><h4>Network Management</h4><p>At vero eos et accusamus et iudignissimos ducimus qui blanditiis praesentiuoluptatum deleniti atque corruptidolores</p></div>
<div class="focus-card" style="left:798px;top:2636px"><h4>Optimization</h4><p>At vero eos et accusamus et iudignissimos ducimus qui blanditiis praesentiuoluptatum deleniti atque corruptidolores</p></div>

<div class="focus-icon" style="left:146px;top:2332px"><svg width="40" height="40" viewBox="0 0 40 40" fill="none" stroke="#fff" stroke-width="2.4"><rect x="7" y="5" width="22" height="30" rx="2"/><path d="M12 13h12M12 19h12M12 25h7M25 31l10-12 3 3-10 12h-3z"/></svg></div>
<div class="focus-icon" style="left:490px;top:2332px"><svg width="40" height="40" viewBox="0 0 40 40" fill="none" stroke="#fff" stroke-width="2.4"><path d="M20 5v30M10 35h20M6 12h28M6 12l-4 10h8zM34 12l-4 10h8z"/><circle cx="20" cy="5" r="2" fill="#fff"/></svg></div>
<div class="focus-icon" style="left:832px;top:2332px"><svg width="40" height="40" viewBox="0 0 40 40" fill="none" stroke="#fff" stroke-width="2.4"><path d="M16 14l14 10-6 1 4 8-3 1-4-8-5 4z" fill="#fff"/><path d="M14 4v5M4 14h5M7 7l3 3M21 7l-3 3"/></svg></div>
<div class="focus-icon" style="left:146px;top:2598px"><svg width="40" height="40" viewBox="0 0 40 40" fill="none" stroke="#fff" stroke-width="2.4"><circle cx="20" cy="20" r="7"/><path d="M20 4v6M20 30v6M4 20h6M30 20h6M9 9l4 4M27 27l4 4M31 9l-4 4M13 27l-4 4"/></svg></div>
<div class="focus-icon" style="left:490px;top:2598px"><svg width="40" height="40" viewBox="0 0 40 40" fill="#fff"><circle cx="20" cy="7" r="4"/><path d="M14 20a6 6 0 0 1 12 0z"/><circle cx="9" cy="27" r="3.5"/><circle cx="31" cy="27" r="3.5"/><path d="M4 37a5 5 0 0 1 10 0zM26 37a5 5 0 0 1 10 0z"/><path d="M20 21v5M11 26h18" stroke="#fff" stroke-width="2"/></svg></div>
<div class="focus-icon" style="left:832px;top:2598px"><svg width="40" height="40" viewBox="0 0 40 40" fill="none" stroke="#fff" stroke-width="2.4"><path d="M6 4v32M6 6h26v20H12"/><rect x="14" y="10" width="12" height="10"/><circle cx="20" cy="15" r="2.5"/></svg></div>

<!-- STATS -->
<section class="stats"></section>
<h2 class="section-title" style="top:2996px">Affiliate Marketing &amp; Ecommerce Growth</h2>
<div class="stat" style="left:108px"><div class="inner"><h5>Affiliates</h5>
<svg width="60" height="60" viewBox="0 0 60 60" fill="#0d1120"><circle cx="30" cy="10" r="5"/><path d="M23 22a7 7 0 0 1 14 0z"/><circle cx="12" cy="26" r="5"/><path d="M5 38a7 7 0 0 1 14 0z"/><circle cx="48" cy="26" r="5"/><path d="M41 38a7 7 0 0 1 14 0z"/><circle cx="30" cy="42" r="5"/><path d="M23 54a7 7 0 0 1 14 0z"/></svg>
<div class="num">100+</div></div></div>
<div class="stat" style="left:356px"><div class="inner"><h5>Advertisers</h5>
<svg width="60" height="60" viewBox="0 0 60 60" fill="#0d1120"><path d="M8 24h8l16-10v32L16 36H8z"/><rect x="36" y="27" width="8" height="6"/><circle cx="50" cy="14" r="4"/><circle cx="50" cy="30" r="4"/><circle cx="50" cy="46" r="4"/></svg>
<div class="num">330+</div></div></div>
<div class="stat" style="left:604px"><div class="inner"><h5>Unique users monthly</h5>
<svg width="60" height="60" viewBox="0 0 60 60" fill="#0d1120"><circle cx="30" cy="14" r="8"/><path d="M18 36a12 12 0 0 1 24 0z"/><path d="M8 40h44l-6 12H14z"/></svg>
<div class="num">3BN</div></div></div>
<div class="stat" style="left:852px"><div class="inner"><h5>Conversions monthly</h5>
<svg width="60" height="60" viewBox="0 0 60 60" fill="#0d1120"><circle cx="30" cy="14" r="10"/><path d="M10 28h40L34 44v12h-8V44z"/><text x="30" y="19" font-size="13" font-weight="700" text-anchor="middle" fill="#fff" font-family="Roboto,sans-serif">$</text></svg>
<div class="num">5 MM</div></div></div>

<!-- TESTIMONIALS -->
<h2 class="section-title" style="top:3467px">What Our Customer Says</h2>
<div class="skyline" role="img" aria-label="Faint city skyline silhouette"></div>

<div class="quote" style="left:107px"><div class="avatar" role="img" aria-label="Customer portrait"></div><h6>HARLAN PIKE</h6><div class="role">Businessman</div>
<p>Sed ut perspiciatis unde omnis iste natus error sit voluptatem accusanti doloremque laudantium, totam rem aperiam, eaque</p><div class="stars">★★★★★</div><div class="qmark">&#8221;</div></div>
<div class="quote" style="left:440px"><div class="avatar" role="img" aria-label="Customer portrait"></div><h6>HARLAN PIKE</h6><div class="role">Businessman</div>
<p>Sed ut perspiciatis unde omnis iste natus error sit voluptatem accusanti doloremque laudantium, totam rem aperiam, eaque</p><div class="stars">★★★★★</div><div class="qmark">&#8221;</div></div>
<div class="quote" style="left:772px"><div class="avatar" role="img" aria-label="Customer portrait"></div><h6>HARLAN PIKE</h6><div class="role">Businessman</div>
<p>Sed ut perspiciatis unde omnis iste natus error sit voluptatem accusanti doloremque laudantium, totam rem aperiam, eaque</p><div class="stars">★★★★★</div><div class="qmark">&#8221;</div></div>
<div class="dots"><i></i><i></i><i style="background:#888"></i><i></i><i></i></div>

<!-- CONTACT -->
<section class="contact"></section>
<div class="frame"></div>
<h2 class="contact" style="all:unset;position:absolute;left:452px;top:4036px;width:296px;background:#0b0c0e;text-align:center;font-family:'Roboto',sans-serif;font-size:38px;font-weight:700;color:#fff">Get In Touch</h2>
<div class="field" style="left:307px;top:4131px;width:287px;height:45px">Full name</div>
<div class="field" style="left:606px;top:4131px;width:291px;height:45px">Email</div>
<div class="field" style="left:307px;top:4191px;width:287px;height:45px">Phone No</div>
<div class="field" style="left:606px;top:4191px;width:291px;height:45px">Company</div>
<div class="field" style="left:307px;top:4251px;width:590px;height:110px">Message</div>
<div class="btn-grey" style="left:525px;top:4415px;width:150px;height:45px;border-radius:2px">SUBMIT NOW <span class="arrow-dot"><svg viewBox="0 0 8 8"><path d="M3 1l3 3-3 3" stroke="#8a8b8e" stroke-width="1.6" fill="none"/></svg></span></div>

<!-- FOOTER -->
<footer class="footer">
  <div class="brand" style="left:118px;top:22px;font-size:44px;line-height:50px">Brindle<br><span style="font-size:16px;letter-spacing:8px;font-weight:700;margin-left:60px">HARBOR</span></div>
  <div class="social" style="left:118px;top:145px;background:#1a56c9"></div>
  <div class="social" style="left:161px;top:145px;background:#2a8ee0"></div>
  <div class="social" style="left:204px;top:145px;background:#d8201e"></div>
  <div class="item" style="left:118px;top:206px;font-size:12px">© 2022 Brindle Harbor. All Rights Reserved.</div>

  <h6 style="left:458px;top:66px">CONTACT US</h6>
  <div class="item" style="left:458px;top:100px"><svg width="12" height="14" viewBox="0 0 12 14" fill="#fff"><path d="M6 0a5 5 0 0 1 5 5c0 4-5 9-5 9S1 9 1 5a5 5 0 0 1 5-5z"/><circle cx="6" cy="5" r="2" fill="#1d1e20"/></svg><span style="margin-left:6px">3971 Lorem Ipsum Dolor Sit</span></div>
  <div class="item" style="left:490px;top:132px">United States</div>
  <div class="item" style="left:458px;top:164px"><svg width="14" height="11" viewBox="0 0 14 11" fill="#fff"><rect width="14" height="11" rx="1"/><path d="M1 1l6 5 6-5" stroke="#1d1e20" fill="none"/></svg><span style="margin-left:4px">Mail&nbsp; : &nbsp;info@brindleharbor.com</span></div>
  <div class="item" style="left:458px;top:197px"><svg width="13" height="13" viewBox="0 0 13 13" fill="#fff"><path d="M2 0l3 3-2 2a8 8 0 0 0 5 5l2-2 3 3-2 2C5 13 0 8 0 2z"/></svg><span style="margin-left:4px">Tel&nbsp;&nbsp;&nbsp;&nbsp; : &nbsp;+1 555 014 2270</span></div>

  <h6 style="left:768px;top:66px">MENU</h6>
  <div class="item" style="left:768px;top:100px">» <span>Home</span></div>
  <div class="item" style="left:768px;top:132px">» <span>About Us</span></div>
  <div class="item" style="left:768px;top:164px">» <span>Reviews</span></div>
  <div class="item" style="left:768px;top:197px">» <span>Contact</span></div>

  <h6 style="left:974px;top:66px">MENU</h6>
  <div class="item" style="left:974px;top:100px">» <span>Publishers</span></div>
  <div class="item" style="left:974px;top:132px">» <span>Advisers</span></div>
  <div class="item" style="left:974px;top:164px">» <span>Privacy Policy</span></div>
  <div class="item" style="left:974px;top:197px">» <span>Terms Of Use</span></div>
</footer>

</body>
</html>
```